Business Card Design Project

Looking for a logo and business card for a Real State Business i will be opening. The name is not choosen yet , but will probably be RKT IMOVEIS.
I was thinking black and silver colors, but am open to nice ideas.
I did add a business card that i liked a lot, am looking for something like that, with logo in black or silver in a black card. The logo i was thinking in the letters RKT as i uploaded or something or little and cute buildings or a house...just ideas, can be any nice logo.
Updates

You guys can add other colors if you want, I like colors very "BRIGHT" and "open", like red, pink, strong colors. almost glow in the dark colors. lol

Designers,

I've increased more 88 dollars in the budget for 1st place cause I will want envelope designs... small and big sizes.

So 1st place is now U$248,00. 

No need to send the envelope designs right now... only the business cards designs.

Thank you.

Industry/Entity Type

Business

Requirements
Must have
• Patricia Souza Ramos

www.RKTimoveisx.com.br

+554193817462

patricia@rktimoveisx.com.br

```html
<!DOCTYPE html>
<html lang="pt">
<head>
<meta charset="utf-8">
<title>RKT Imoveis — Stationery</title>
<link rel="stylesheet" href="https://fonts.googleapis.com/css2?family=Barlow:wght@300;400;600;700&family=Tinos:wght@400;700&display=swap">
<style>
  :root {
    --pink: #ff0080;
    --ink: #111111;
    --charcoal: #2b2a2b;
    --paper: #ffffff;
    --rule: #9a9a9a;
    --caption: #8a8a8a;
    --body-text: #333333;
  }
  * { box-sizing: border-box; margin: 0; padding: 0; }
  html, body { width: 1200px; height: 800px; overflow: hidden; background: var(--paper); }
  .board { position: relative; width: 1200px; height: 800px; font-family: "Barlow", sans-serif; }

  .project-caption {
    position: absolute; left: 30px; top: 30px;
    font-weight: 300; font-size: 13px; letter-spacing: 0.6px; color: var(--caption);
  }

  .brand-mark {
    position: absolute; font-family: "Barlow", sans-serif; font-weight: 700;
    color: var(--pink); line-height: 1; letter-spacing: -1px;
  }

  /* Letterhead */
  .letterhead {
    position: absolute; left: 138px; top: 70px; width: 498px; height: 705px;
    border: 1px solid var(--rule); background: var(--paper);
  }
  .letterhead .brand-mark { left: 226px; top: 6px; font-size: 34px; }
  .letter-body {
    position: absolute; left: 68px; top: 172px; width: 340px;
    font-family: "Tinos", serif; font-size: 7px; line-height: 9.5px; color: var(--body-text);
  }
  .letter-intro { margin-bottom: 28px; }
  .letter-date { text-align: right; margin-right: -25px; margin-bottom: 36px; }
  .letter-subject { font-weight: 700; margin-bottom: 26px; }
  .letter-body p { margin-bottom: 9px; text-align: justify; }
  .letter-signature {
    display: block; width: 60px; height: 26px; margin: 2px 0 0 0;
    background: linear-gradient(90deg, #d8d8d8, #b9b9b9);
  }
  .letter-footer {
    position: absolute; left: 0; right: 0; bottom: 22px; text-align: center;
    font-weight: 700; font-size: 7px; letter-spacing: 0.3px; color: var(--pink);
  }

  /* Business cards */
  .card { position: absolute; top: 200px; width: 119px; height: 189px; }
  .card-front { left: 608px; background: var(--pink); }
  .card-back { left: 738px; background: var(--charcoal); }
  .card-front .brand-mark { left: 10px; top: 6px; font-size: 30px; color: var(--ink); }
  .card-back .brand-mark { left: 14px; top: 6px; font-size: 30px; }
  .card-details {
    position: absolute; left: 12px; top: 88px; font-size: 6px; line-height: 7px; color: var(--ink);
  }
  .card-name { font-weight: 700; letter-spacing: 0.2px; }
  .card-contact { font-weight: 400; color: #3a0020; }
  .card-web { margin-top: 14px; font-weight: 700; letter-spacing: 0.2px; }

  /* Envelope */
  .envelope {
    position: absolute; left: 516px; top: 432px; width: 546px; height: 274px;
    border: 1px solid var(--rule); background: var(--paper);
  }
  .envelope-flap { position: absolute; left: 0; top: 0; }
  .envelope .brand-mark { left: 250px; top: 22px; font-size: 34px; }
  .envelope-web {
    position: absolute; left: 0; right: 0; top: 127px; text-align: center;
    font-weight: 700; font-size: 7px; letter-spacing: 0.3px; color: var(--pink);
  }
</style>
</head>
<body>
<main class="board">
  <p class="project-caption">PROJECT RKT LOGO &amp; BUSINESS CARD / APR 2013</p>

  <section class="letterhead">
    <div class="brand-mark">RKT</div>
    <div class="letter-body">
      <div class="letter-intro">Vi invitiamo a leggere<br>questi documenti accuratamente!</div>
      <div class="letter-date">Febbraio 2010</div>
      <div class="letter-subject">Aggiornamento dei dati 2010</div>
      <p>Gentili Sigg.re e Sigg.ri,</p>
      <p>Nel quadro dell'aggiornamento annuale della Vostra scheda nel nostro archivio clienti, Vi preghiamo di verificare la correttezza e completezza dei Vostri dati da noi registrati e di rettificarli, se è necessario, presso il nostro ufficio. Solamente così, l'archivio riporterà i dati più attuali! La Vostra scheda di base e il suo aggiornamento sono gratuiti.</p>
      <p>I Vostri dati attualmente registrati, li troverete nel modulo allegato, che Vi preghiamo di completare nel caso in cui voleste passare ad un ordine soggetto a spese. La registrazione di base gratuita e il suo aggiornamento possono essere effettuate da Voi stessi sul nostro sito, cliccando su registrazione.</p>
      <p>Vi ringraziamo ancora molto sinceramente per la Vostra fiducia nel nostro lavoro.</p>
      <div>Porgiamo distinti saluti</div>
      <span class="letter-signature" role="img" aria-label="Handwritten signature"></span>
      <div>La Vostra redazione</div>
    </div>
    <div class="letter-footer">WWW.RKTIMOVEISX.COM.BR</div>
  </section>

  <section class="card card-front">
    <div class="brand-mark">RKT</div>
    <div class="card-details">
      <div class="card-name">PATRICIA SOUZA RAMOS</div>
      <div class="card-contact">PATRICIA@RKTIMOVEISX.COM.BR</div>
      <div class="card-contact">+55 419381 7462</div>
      <div class="card-web">WWW.RKTIMOVEISX.COM.BR</div>
    </div>
  </section>

  <section class="card card-back">
    <div class="brand-mark">RKT</div>
  </section>

  <section class="envelope">
    <svg class="envelope-flap" width="546" height="110" viewBox="0 0 546 110" aria-hidden="true">
      <polyline points="0,0 29,106 517,106 546,0" fill="none" stroke="#9a9a9a" stroke-width="1"/>
    </svg>
    <div class="brand-mark">RKT</div>
    <div class="envelope-web">WWW.RKTIMOVEISX.COM.BR</div>
  </section>
</main>
</body>
</html>
```